Harborline Health - Figma **Updated**

Below are the instructions for the website redesign project for Harborline Health:
Website Design Review
• Color Scheme: Maintain the clean and professional Red and White color theme.
• Layout: Ensure the layout is straightforward and user-friendly.
• Typography: Use modern and easy-to-read font choices.
• Mobile Optimization: Ensure the website is fully optimized for mobile devices.
Design Requirements
• Clean, Minimalistic, and Responsive Design:
o The design should be clean, easy to navigate, and modern.
o The primary user base consists of seniors, so accessibility and simplicity are key.
• Location-Based Pages:
o Develop pages for each medical clinic and pharmacy location to provide a unique digital presence for each branch.
• Current Content:
o The current content is good but needs to be more efficient and user-friendly for patients.
• Doctor and Staff Introductions:
o Include an introduction section for our doctors and staff to build trust with visitors.
• Custom Design:
o Please avoid using ready-made themes. The preferred design source is a Figma file for development with Elementor.
• Logo:
o See the attached logo for reference.
Key Sections to Enhance
• My Team Section: Enhance this section to highlight healthcare professionals and build trust with visitors.
• Footer Section: Improve the footer by including more links to important sections and social media icons. Ensure the Quorvex Logo is included on all footers.
• Contact Us Page: Enhance the Contact Us page to include options to upload documents and select specific locations or services.
• Intake Form Page: Improve the Intake Form page by implementing user-friendly and accessible forms.
• Patient Consent Forms: Implement patient consent forms for marketing purposes that are integrated with our database and software.
Websites for Design Inspiration
1. Tarnwell Health: https://www.tarnwellhealth.example/?form=MG0AV3
• What We Like: The overall theme, font choices, and the look and feel of the website.
2. SnugDose: https://www.snugdose.example/
• What We Like: The clean and intuitive layout.
3. BrightFern: https://brightfern.example/
• What We Like: Everything about the design, including aesthetics, usability, and functionality.

Color and Theme Ideas
• Clinic Red, Pharmacy Green, Blue Branding:
o https://www.tarnwellhealth.example/?form=MG0AV3
o https://lorvanmd.example/
o https://www.kpq.example/en/financing?form=MG0AV3
o https://roamingvisitcare.example/
Design Inspirations
• https://brightfern.example/
• https://www.snugdose.example/
• https://www.galdens.example/online/pharmacy/
• https://pharmacy.orvella.example/
• https://www.dosecrate.example/how-it-works
• https://farcarerx.example/
Pages to Design
1. Landing Page (Clinic): https://harborlinehealth.ca/
2. Medical Clinic Intake Instructions: https://harborlinehealth.ca/medical-clinic-intake-form/
3. My Team Page and Introduction for Each Team Member
4. Book Appointment: https://harborlinehealth.ca/book-appointment/
o Dropdown/Options on the page:
1. Family Practice
2. Walk-In Telehealth
3. Travel Consultation – Telehealth
4. Private Consult with Nurse Practitioner
5. Pharmacy: https://harborlinehealth.ca/pharmacy/ (Pay attention to Pop-up Design)
6. Home Monitoring: https://harborlinehealth.ca/home-monitoring-program/
7. Home Health Care: https://harborlinehealth.ca/home-healthcare/
8. Contact Us: https://harborlinehealth.ca/contact/
9. Resources: https://harborlinehealth.ca/resources/ (We need Blog and News)
10. Blog Template: https://harborlinehealth.ca/2025/02/14/find-doctor-surrey/ (Need massive improvement and responsiveness)
11. Join My Team: https://harborlinehealth.ca/career/
Additional Improvements
• Header, Footer, and Banners: Massive improvement needed (Video integration would be great).
• Privacy Policy | Cookies | Terms and Conditions: Improvements needed.
Comments for Tovin
• Footer: We need a footer like SnugDose.
• Mobile Design: Ensure mobile design is similar to SnugDose.
• Social Media and Blogs: Integration needed.
• Email/Marketing List Sign-Up: Implement a sign-up option for patients/visitors.
• Google Reviews: Integrate Google reviews.
• Clinic Videos and Pictures: Include multimedia content.
• Keyword Optimization: Content will be rephrased for keyword optimization (keywords list provided).
• Keywords: I will ask that certain keywords [e.g. from blog] to link certain website page automatically
• Quorvex Logo: Include Quorvex logo at the bottom.
• Online Appointment Dropdown: Add dropdown options for different appointment types.
Please proceed with the necessary updates and preparations. Once you have the revised design ready in Figma, kindly send it over for approval.
We currently use the Harborline Part with Vector and Tag line as the logo for both our Clinic and Pharmacy businesses. However, we have several design considerations and requests:

Banner Designs: What will each banner look like?

Other Pages: How will the other pages appear?

Header and Footer: The current designs for the header and footer are not satisfactory.

Text Placement and Font: We need improved text placement and a better font choice.

Team Members' Pictures: Use actual pictures of our team members.

Logos for Specific Services: Please update the logo/Vector for services such as Chronic Complex Care and Diagnostic Investigations.

Location-Based Pages: We need separate pages for the Pharmacy and Clinic, with links specific to each city—Surrey and White Rock.
Looking forward to seeing the improvements!

```html
<!DOCTYPE html>
<html lang="en">
<head>
<meta charset="utf-8">
<title>Harborline Health — Clinic &amp; Pharmacy Website</title>
<link href="https://fonts.googleapis.com/css2?family=Poppins:wght@400;500;600;700&display=swap" rel="stylesheet">
<style>
:root{
  --navy:#2b2f83;
  --navy-dark:#23266e;
  --red:#e31e2e;
  --green:#1ea54a;
  --pink:#fbe3e6;
  --lav:#eef0f8;
  --ink:#33364f;
  --muted:#6b6e85;
  --line:#e4e5ef;
  --white:#ffffff;
}
*{box-sizing:border-box;margin:0;padding:0}
html,body{width:1200px;height:5055px;overflow:hidden}
body{font-family:"Poppins",sans-serif;color:var(--ink);background:linear-gradient(180deg,#e9ebf7 0,#f5f6fb 500px,#ffffff 1200px);position:relative}
.abs{position:absolute}
.photo{position:absolute;border-radius:3px}
.ph-warm{background:linear-gradient(135deg,#d9c8bd,#b58f7c 55%,#7a5f57)}
.ph-cool{background:linear-gradient(135deg,#dfe4ea,#a9b4c2 55%,#6f7b8c)}
.ph-clinic{background:linear-gradient(135deg,#eef0f3,#c9cfd8 50%,#8e98a8)}
.ph-team{background:linear-gradient(160deg,#e8edf3,#b9c6d6 50%,#7d90a8)}

/* brand block */
.brand{position:absolute;left:0;right:0;top:78px;display:flex;justify-content:center;align-items:center;gap:14px}
.brand-mark{width:46px;height:46px;background:var(--red);border-radius:4px}
.brand-name{font-size:38px;font-weight:700;color:var(--navy);line-height:1}
.brand-tag{font-size:15px;color:var(--red);margin-top:4px}
.brand-side{font-size:22px;font-weight:600;color:var(--navy);line-height:1.25;margin-left:8px}

/* shared */
.logo-sm{display:flex;align-items:center;gap:3px}
.logo-sm .sq{background:var(--red);border-radius:1px}
.logo-sm b{color:var(--navy);font-weight:700}
.btn{display:inline-block;border-radius:2px;color:#fff;font-weight:500;text-align:center}
.btn-red{background:var(--red)}
.btn-green{background:var(--green)}
.h-title{font-weight:400;color:var(--navy);text-align:center}
.h-title em{font-style:normal;color:var(--red)}
.badge{background:#d5d8e8;border-radius:50%}
.badge-rect{background:#d5d8e8;border-radius:2px}

/* ===== desktop ===== */
.desk{position:absolute;left:175px;top:225px;width:594px;height:2054px;background:#fff;box-shadow:0 6px 30px rgba(43,47,131,.12);overflow:hidden}
.desk section{position:absolute;left:0;width:594px}
.d-top{top:0;height:10px;background:var(--navy);color:#fff;font-size:3.6px;padding:0 14px;display:flex;align-items:center;justify-content:space-between}
.d-top span.pill{border:0.5px solid #fff;padding:0 4px;border-radius:1px}
.d-nav{top:10px;height:40px;display:flex;align-items:center;padding:0 22px;justify-content:space-between}
.d-nav ul{list-style:none;display:flex;gap:13px;font-size:4.6px;color:var(--ink)}
.d-nav li.on{color:var(--red);border-bottom:1px solid var(--red);padding-bottom:2px}
.d-hero{top:50px;height:288px;background:var(--pink)}
.d-hero .copy{position:absolute;left:52px;top:80px;width:190px}
.d-hero .w{font-size:12px;color:var(--red)}
.d-hero h1{font-size:14px;color:var(--navy);font-weight:600;line-height:1.2}
.d-hero .tag{font-size:9.5px;color:var(--red);font-weight:500;margin-bottom:8px}
.d-hero p{font-size:4.6px;line-height:1.55;color:var(--ink)}
.d-hero .btns{display:flex;gap:6px;margin-top:12px}
.d-hero .btns .btn{font-size:4.4px;padding:4px 9px}
.play{position:absolute;width:22px;height:22px;border-radius:50%;background:var(--red)}
.play:after{content:"";position:absolute;left:9px;top:6px;border-left:7px solid #fff;border-top:5px solid transparent;border-bottom:5px solid transparent}
.dots{position:absolute;display:flex;gap:3px}
.dots i{width:3px;height:3px;border-radius:50%;background:#fff;opacity:.7}
.dots i.on{background:var(--red);opacity:1}
.d-strip{top:338px;height:61px;padding:8px 52px;display:flex;gap:40px}
.strip-lbl{font-size:4.6px;font-weight:600;color:var(--navy);margin-bottom:6px}
.strip-row{display:flex;gap:12px;align-items:center}

.d-serv{top:399px;height:288px}
.d-serv h2{position:absolute;top:38px;width:100%;font-size:14px}
.d-serv .sub{position:absolute;top:58px;width:100%;text-align:center;font-size:4.6px;color:var(--navy);font-weight:500}
.s-card{position:absolute;top:88px;width:118px;height:141px;border:0.6px solid var(--line);border-radius:3px;padding:7px}
.s-card .ico{width:14px;height:14px;border-radius:50%;background:var(--pink);float:left;margin-right:5px}
.s-card h3{font-size:5.2px;color:var(--navy);font-weight:600;line-height:1.3}
.s-card p{clear:both;font-size:3.6px;line-height:1.5;color:var(--muted);padding-top:6px}
.s-card .photo{left:7px;right:7px;bottom:7px;height:58px}
.arrow-ne{position:absolute;right:8px;top:8px;width:6px;height:6px}
.center-btn{position:absolute;left:50%;transform:translateX(-50%);font-size:4.4px;padding:4px 10px}

.d-about{top:687px;height:221px}
.d-mission{top:908px;height:171px;background:var(--navy);color:#fff}
.d-mission h2{position:absolute;left:200px;top:48px;font-size:11px;font-weight:400}
.d-mission h2 em{font-style:normal;color:var(--red)}
.d-mission p{position:absolute;left:200px;top:66px;width:300px;font-size:4.4px;line-height:1.6}
.about-photo{left:98px;top:10px;width:192px;height:251px;z-index:2}
.yrs{position:absolute;z-index:3;background:var(--green);color:#fff;border-radius:12px;font-weight:700;display:flex;align-items:center;gap:4px}
.yrs small{font-weight:400;line-height:1.2}
.d-about .copy{position:absolute;left:316px;top:42px;width:180px}
.d-about h2{font-size:11px;font-weight:400;color:var(--navy)}
.d-about h2 em{font-style:normal;color:var(--red)}
.d-about .lead{font-size:7px;line-height:1.4;color:var(--ink);margin:4px 0}
.d-about .strong{font-size:4.8px;font-weight:600;color:var(--navy);line-height:1.4;margin-bottom:4px}
.d-about p{font-size:3.8px;line-height:1.55;color:var(--muted)}

.d-rev{top:1079px;height:265px;background:var(--lav)}
.d-rev h2{position:absolute;top:40px;width:100%;font-size:12px}
.d-rev .sub{position:absolute;top:56px;width:100%;text-align:center;font-size:4.4px;color:var(--navy);font-weight:600}
.d-rev .score{position:absolute;top:65px;width:100%;text-align:center;font-size:3.8px}
.stars{color:var(--red);letter-spacing:.5px}
.r-card{position:absolute;top:92px;width:122px;height:108px;background:#fff;border-radius:3px;padding:7px}
.r-head{display:flex;align-items:center;gap:5px}
.avatar{width:11px;height:11px;border-radius:50%;color:#fff;font-size:5px;display:flex;align-items:center;justify-content:center;font-weight:600}
.r-card b{font-size:4.4px;color:var(--navy);display:block}
.r-card small{font-size:3.4px;color:var(--muted)}
.r-card .stars{font-size:6px;display:block;margin:4px 0}
.r-card p{font-size:3.6px;line-height:1.55;color:var(--muted)}
.g-dot{position:absolute;right:7px;top:8px;width:7px;height:7px;border-radius:50%;border:1px solid #b7bacb}
.circ-arrow{position:absolute;width:11px;height:11px;border-radius:50%;border:0.6px solid #a7a9c0}

.d-res{top:1344px;height:300px}
.d-res h2{position:absolute;top:49px;width:100%;font-size:12px}
.d-res .sub{position:absolute;top:65px;width:100%;text-align:center;font-size:4.4px;color:var(--navy);font-weight:500}
.b-card{position:absolute;top:88px;width:112px;height:143px;border:0.6px solid var(--line);border-radius:3px;padding:6px}
.b-card .photo{position:relative;display:block;height:58px}
.b-card .dt{font-size:3.6px;color:var(--red);margin-top:6px}
.b-card h3{font-size:4.6px;color:var(--navy);font-weight:600;line-height:1.4;margin-top:2px}
.b-card .go{position:absolute;left:6px;bottom:6px;width:9px;height:9px;border-radius:50%;border:0.6px solid var(--red)}

.d-faq{top:1644px;height:202px;background:var(--pink)}
.d-faq .left{position:absolute;left:52px;top:36px;width:150px}
.kick{font-size:4.4px;font-weight:600;color:var(--navy)}
.d-faq h2{font-size:13px;font-weight:400;color:var(--red);line-height:1.15;margin:4px 0 5px}
.d-faq h2 em{font-style:normal;color:var(--navy)}
.d-faq .left p{font-size:3.8px;line-height:1.5;color:var(--muted)}
.emerg{display:flex;align-items:center;gap:6px;background:#fff;border-radius:3px;padding:7px;margin-top:10px}
.emerg .badge{width:14px;height:14px;background:var(--pink)}
.emerg span{font-size:3.8px;color:var(--navy);line-height:1.5}
.emerg strong{color:var(--red);font-weight:600}
.faq-list{position:absolute;left:318px;top:40px;width:222px}
.faq-item{border-bottom:0.6px solid #f0b9c0;font-size:4.4px;color:var(--navy);padding:4px 0;display:flex;justify-content:space-between}
.faq-item .chev{color:var(--red)}
.faq-ans{font-size:3.6px;color:var(--muted);line-height:1.5;padding:2px 0 4px}

.d-foot{top:1846px;height:208px;background:var(--navy);color:#fff}
.d-foot .logo{position:absolute;left:60px;top:24px}
.d-foot .name{font-size:15px;font-weight:700}
.d-foot .tg{font-size:5px;opacity:.85}
.socials{display:flex;gap:3px}
.socials i{display:block;border-radius:50%;border:0.6px solid #fff}
.d-foot .links{position:absolute;left:190px;top:26px;font-size:4.6px;line-height:2.2}
.d-foot .links b{font-weight:600}
.loc{position:absolute;left:298px;width:252px;font-size:4px;border-bottom:0.5px solid rgba(255,255,255,.3);padding:3px 0;display:flex;justify-content:space-between}
.loc b{font-weight:600}
.loc .c{display:inline-block;width:4px;height:4px;background:var(--red);margin-right:3px}
.loc .c.g{background:var(--green)}
.d-foot .legal{position:absolute;left:52px;bottom:22px;right:52px;font-size:3.6px;opacity:.85;display:flex;gap:40px}

/* ===== mobile ===== */
.mob{position:absolute;left:802px;top:225px;width:220px;height:4750px;background:#fff;box-shadow:0 6px 30px rgba(43,47,131,.12);overflow:hidden}
.mob section{position:absolute;left:0;width:220px}
.m-top{top:0;height:79px;background:var(--navy);color:#fff;text-align:center;padding:14px 16px 0;font-size:5.6px;line-height:1.5}
.m-top .pill{display:inline-block;border:0.6px solid #fff;padding:3px 12px;margin-top:6px;font-size:5.2px}
.m-nav{top:79px;height:49px;display:flex;align-items:center;justify-content:space-between;padding:0 14px}
.burger{width:18px}
.burger i{display:block;height:1.4px;background:var(--navy);margin:3px 0}
.m-hero{top:128px;height:412px;background:var(--pink);text-align:center}
.m-hero .w{padding-top:38px;font-size:14px;color:var(--red)}
.m-hero h1{font-size:15px;color:var(--navy);font-weight:600}
.m-hero .tag{font-size:10px;color:var(--red);font-weight:500;margin-top:2px}
.m-hero p{font-size:6.6px;line-height:1.6;padding:8px 18px 0}
.m-hero .btns{display:flex;justify-content:center;gap:8px;margin-top:18px}
.m-hero .btns .btn{font-size:6px;padding:6px 14px}
.m-hero .photo{left:10px;right:10px;top:300px;height:151px;position:absolute}

.m-strip{top:540px;height:215px;padding:12px 12px}
.m-strip .strip-lbl{font-size:7px;margin-bottom:8px}

.m-serv{top:755px;height:893px}
.m-serv h2{position:absolute;top:16px;width:100%;font-size:15px}
.m-serv .sub{position:absolute;top:38px;width:100%;text-align:center;font-size:6.4px;color:var(--navy);font-weight:500;padding:0 20px;line-height:1.4}
.m-card{position:absolute;left:10px;width:200px;height:235px;border:0.6px solid var(--line);border-radius:3px;padding:12px}
.m-card .ico{width:24px;height:24px;border-radius:50%;background:var(--pink);float:left;margin-right:7px}
.m-card h3{font-size:8px;color:var(--navy);font-weight:600;line-height:1.3;padding-top:3px}
.m-card p{clear:both;font-size:6px;line-height:1.55;color:var(--muted);padding-top:14px}
.m-card .photo{left:12px;right:12px;bottom:12px;height:108px}

.m-about{top:1648px;height:540px;text-align:center}
.m-about h2{padding-top:20px;font-size:14px;font-weight:400;color:var(--navy)}
.m-about h2 em{font-style:normal;color:var(--red)}
.m-about .lead{font-size:9.5px;line-height:1.45;padding:6px 14px 0}
.m-about .strong{font-size:7px;font-weight:600;color:var(--navy);line-height:1.45;padding:10px 20px 0}
.m-about p{font-size:6px;line-height:1.6;color:var(--muted);padding:10px 14px 0}
.m-mission{top:2187px;height:284px;background:var(--navy);color:#fff;text-align:center}
.m-mission h2{position:absolute;top:68px;width:100%;font-size:13px;font-weight:400}
.m-mission h2 em{font-style:normal;color:var(--red)}
.m-mission p{position:absolute;top:90px;left:14px;right:14px;font-size:6.8px;line-height:1.65}

.m-rev{top:2471px;height:314px;background:var(--lav);text-align:center}
.m-rev h2{padding-top:14px;font-size:13px}
.m-rev .sub{font-size:6.4px;color:var(--navy);font-weight:600;padding:4px 30px 0;line-height:1.4}
.m-rev .score{font-size:6px;margin-top:3px}
.m-rev .r-card{left:10px;top:90px;width:200px;height:168px;text-align:left;padding:12px}
.m-rev .avatar{width:22px;height:22px;font-size:9px}
.m-rev .r-card b{font-size:7px}
.m-rev .r-card small{font-size:5.6px}
.m-rev .r-card .stars{font-size:10px}
.m-rev .r-card p{font-size:6px}
.m-rev .g-dot{width:11px;height:11px;right:12px;top:14px}

.m-res{top:2785px;height:863px;text-align:center}
.m-res h2{padding-top:20px;font-size:14px}
.m-res .sub{font-size:6.4px;color:var(--navy);font-weight:500;margin-top:6px}
.m-res .b-card{left:10px;width:200px;height:236px;padding:12px;text-align:left}
.m-res .b-card .photo{height:108px}
.m-res .b-card .dt{font-size:6px;margin-top:10px}
.m-res .b-card h3{font-size:8px}
.m-res .b-card .go{width:16px;height:16px;left:12px;bottom:14px}

.m-faq{top:3648px;height:618px;background:var(--pink);text-align:center}
.m-faq .kick{padding-top:22px;font-size:7px}
.m-faq h2{font-size:14px;font-weight:400;color:var(--red);line-height:1.2;margin-top:6px}
.m-faq h2 em{font-style:normal;color:var(--navy)}
.m-faq .intro{font-size:6.2px;line-height:1.55;color:var(--muted);padding:8px 18px 0}
.m-faq .faq-list{position:static;width:auto;margin:22px 18px 0;text-align:left}
.m-faq .faq-item{font-size:7px;padding:9px 0;line-height:1.35}
.m-faq .faq-ans{font-size:5.8px}
.m-faq .emerg{flex-direction:column;margin:22px 18px 0;padding:12px}
.m-faq .emerg .badge{width:22px;height:22px}
.m-faq .emerg span{font-size:6.4px;text-align:center}

.m-foot{top:4285px;height:465px;background:var(--navy);color:#fff}
.m-foot .logo{position:absolute;left:14px;top:30px}
.m-foot .name{font-size:26px;font-weight:700;line-height:1}
.m-foot .tg{font-size:8px;opacity:.85;margin-top:2px}
.m-foot .ql{position:absolute;left:12px;top:86px;font-size:8px;font-weight:600}
.m-foot .cols{position:absolute;left:12px;top:104px;display:flex;gap:46px;font-size:7px;line-height:1.9;opacity:.9}
.m-foot .loc{left:12px;width:196px;font-size:6px;padding:6px 0}
.m-foot .det{position:absolute;left:24px;font-size:5.8px;opacity:.9;line-height:2.6}
.m-foot .socials{position:absolute;left:0;right:0;top:395px;justify-content:center}
.m-foot .legal{position:absolute;top:420px;width:100%;text-align:center;font-size:5.6px;opacity:.85;line-height:2}
</style>
</head>
<body>

<header class="brand">
  <div class="brand-mark"></div>
  <div>
    <div class="brand-name">Harborline</div>
    <div class="brand-tag">Your Partner in Health</div>
  </div>
  <div class="brand-side">Medical Clinic<br>Pharmacy</div>
</header>

<!-- ================= DESKTOP ================= -->
<main class="desk">
  <section class="d-top"><span>Proudly Canadian and locally owned and operated. Our doctors and nurse practitioners are now accepting new patients.</span><span class="pill">Download Intake Forms</span></section>

  <section class="d-nav">
    <div class="logo-sm"><span class="sq" style="width:8px;height:8px"></span><b style="font-size:8px">Harborline</b><span style="font-size:4px;color:var(--navy);margin-left:3px;line-height:1.2">Medical Clinic<br>Pharmacy</span></div>
    <ul><li class="on">Home</li><li>Medical Clinic</li><li>Pharmacy</li><li>Home Monitoring</li><li>Home Healthcare</li><li>Resources</li><li>Contact Us</li></ul>
    <span class="btn btn-red" style="font-size:4.4px;padding:4px 8px">Book Appointment</span>
  </section>

  <section class="d-hero">
    <div class="copy">
      <div class="w">Welcome to</div>
      <h1>Harborline Medical Clinic</h1>
      <div class="tag">Your Partner In Health</div>
      <p>We are a trusted family doctor in white rock and surrey, committed to offering reliable family doctors in surrey with a focus on providing convenient medical care in surrey.</p>
      <div class="btns"><span class="btn btn-red">Book Appointment</span><span class="btn btn-green">Join Our Team</span></div>
      <div style="font-size:5px;color:var(--navy);margin-top:14px">1 / 4</div>
    </div>
    <div class="photo ph-clinic" style="left:290px;top:29px;width:276px;height:216px" role="img" aria-label="Two smiling doctors in white coats in a bright clinic"></div>
    <div class="play" style="left:280px;top:126px"></div>
    <div class="dots" style="left:412px;top:236px"><i class="on"></i><i></i><i></i><i></i></div>
  </section>

  <section class="d-strip">
    <div>
      <div class="strip-lbl">Member of</div>
      <div class="strip-row"><span class="badge-rect" style="width:46px;height:16px"></span><span class="badge-rect" style="width:50px;height:16px"></span><span class="badge" style="width:16px;height:16px"></span></div>
    </div>
    <div>
      <div class="strip-lbl">Licensed by</div>
      <div class="strip-row"><span class="badge-rect" style="width:46px;height:16px"></span><span class="badge" style="width:16px;height:16px"></span><span class="badge-rect" style="width:40px;height:16px"></span><span class="badge" style="width:16px;height:16px"></span><span class="badge-rect" style="width:40px;height:16px"></span></div>
    </div>
  </section>

  <section class="d-serv">
    <h2 class="h-title">Our <em>services</em></h2>
    <div class="sub">Convenient, Quality Care in Surrey and White Rock</div>
    <article class="s-card" style="left:100px"><span class="ico"></span><h3>Chronic and<br>complex care</h3><p>Our experienced family doctors in surrey and white rock offer high-quality care for chronic conditions.</p><div class="photo ph-warm" role="img" aria-label="Caregiver assisting an older patient at home"></div></article>
    <article class="s-card" style="left:237px"><span class="ico"></span><h3>Diagnostic<br>investigation</h3><p>Our medical clinic near me provides a wide range of diagnostic tests and procedures.</p><div class="photo ph-cool" role="img" aria-label="Lab technician working with a microscope"></div></article>
    <article class="s-card" style="left:374px"><span class="ico"></span><h3>Full family care<br>services</h3><p>We offer comprehensive family doctor services for all ages, including adults and youth.</p><div class="photo ph-warm" role="img" aria-label="Family visiting a doctor together"></div></article>
    <span class="btn btn-red center-btn" style="top:250px">View All Services</span>
  </section>

  <section class="d-mission">
    <h2>Mission <em>statement</em></h2>
    <p>Our mission is to be the best walk-in clinic in Surrey and a top-rated medical clinic in Surrey, leading the way in innovation and patient care. We aim to provide affordable healthcare that is empathetic, efficient, and accessible to all.</p>
  </section>

  <section class="d-about" style="overflow:visible">
    <div class="photo ph-team about-photo" role="img" aria-label="Group of doctors and nurses standing together"></div>
    <div class="yrs" style="left:160px;top:2px;padding:3px 8px;font-size:9px">10+<small style="font-size:3.6px">Years of working<br>experience</small></div>
    <div class="copy">
      <h2>About <em>us</em></h2>
      <div class="lead">We're an established, forward thinking family practice in white rock/south surrey.</div>
      <div class="strong">We're proud to provide top-notch healthcare services at Harborline in white rock.</div>
      <p>We are a trusted family doctor in White Rock and Surrey, committed to offering reliable family doctors in Surrey with a focus on providing convenient medical care. Our medical clinic is equipped with the latest technology and staffed by a skilled team.</p>
      <span class="btn btn-red" style="font-size:4px;padding:3px 8px;margin-top:8px">Explore More</span>
    </div>
  </section>

  <section class="d-rev">
    <h2 class="h-title">What our <em>client says</em></h2>
    <div class="sub">Harborline Pharmacy &amp; Vaccine Clinic - White Rock/South Surrey</div>
    <div class="score">Excellent <span class="stars">★★★★★</span> 4.9 based on 199 reviews</div>
    <span class="circ-arrow" style="left:36px;top:140px"></span>
    <article class="r-card" style="left:104px"><span class="g-dot"></span><div class="r-head"><span class="avatar" style="background:var(--green)">M</span><div><b>Mara Ellison</b><small>5 Days Ago</small></div></div><span class="stars">★★★★★</span><p>I was able to speak to a doctor, receive a prescription from the doctor through the clinic and pick up my prescription all within one hour! Very pleasant.</p></article>
    <article class="r-card" style="left:236px"><span class="g-dot"></span><div class="r-head"><span class="avatar" style="background:var(--navy)">N</span><div><b>Neal Torvik</b><small>6 Weeks Ago</small></div></div><span class="stars">★★★★★</span><p>We moved into the white rock area from today. After searching for a pharmacy for a while, we found one that suits our needs and the staff are great.</p></article>
    <article class="r-card" style="left:368px"><span class="g-dot"></span><div class="r-head"><span class="avatar" style="background:var(--red)">L</span><div><b>Lena Ruiz</b><small>2 Weeks Ago</small></div></div><span class="stars">★★★★★</span><p>My husband and I have had great experiences with the pharmacists and staff here. Always helpful and friendly, and quick to help.</p></article>
    <span class="circ-arrow" style="left:546px;top:140px"></span>
    <span class="btn btn-red center-btn" style="top:212px">View All Reviews</span>
  </section>

  <section class="d-res">
    <h2 class="h-title">Harborline <em>Resources</em></h2>
    <div class="sub">Explore the latest news and resources.</div>
    <article class="b-card" style="left:106px"><div class="photo ph-warm" role="img" aria-label="Toddler sitting at a table with food"></div><div class="dt">Feb 18, 2025</div><h3>Why your toddler won't eat and when to seek care</h3><span class="go"></span></article>
    <article class="b-card" style="left:242px"><div class="photo ph-cool" role="img" aria-label="Doctor talking with a patient"></div><div class="dt">Feb 14, 2025</div><h3>What to do if you don't have a family doctor in white rock, south surrey, and surrey</h3><span class="go"></span></article>
    <article class="b-card" style="left:378px"><div class="photo ph-warm" role="img" aria-label="Nurse checking an older patient at home"></div><div class="dt">Feb 14, 2025</div><h3>Enhancing patient care with Harborline pharmacy's home monitoring program</h3><span class="go"></span></article>
    <span class="btn btn-red center-btn" style="top:255px">View All Resources</span>
  </section>

  <section class="d-faq">
    <div class="left">
      <div class="kick">Frequently asked questions</div>
      <h2>Helping you <em>understand</em> healthcare</h2>
      <p>Here to make your experience as seamless as possible: explore answers to common questions about our services, policies, and patient care.</p>
      <div class="emerg"><span class="badge"></span><span>We always take care of your smile<br><strong>24/7 Emergency</strong><br>604-555-0199</span></div>
    </div>
    <div class="faq-list">
      <div class="faq-item"><span>What should I bring to my first appointment?</span><span class="chev">⌃</span></div>
      <div class="faq-ans">For your first visit, please bring a valid ID, your insurance card, any current medications or a list of them, and any relevant medical records.</div>
      <div class="faq-item"><span>How do I schedule an appointment?</span><span class="chev">⌄</span></div>
      <div class="faq-item"><span>What insurance plan do you accept?</span><span class="chev">⌄</span></div>
      <div class="faq-item"><span>Can I get a prescription refill without an appointment?</span><span class="chev">⌄</span></div>
      <div class="faq-item"><span>What should I expect during my first visit?</span><span class="chev">⌄</span></div>
      <div class="faq-item"><span>How are treatment plans customized for individual need?</span><span class="chev">⌄</span></div>
    </div>
  </section>

  <section class="d-foot">
    <div class="logo">
      <div class="logo-sm"><span class="sq" style="width:14px;height:14px"></span><span class="name">Harborline</span></div>
      <div class="tg" style="margin-left:17px">Your Partner in Health</div>
      <div class="socials" style="margin:8px 0 0 17px"><i style="width:7px;height:7px"></i><i style="width:7px;height:7px"></i><i style="width:7px;height:7px"></i><i style="width:7px;height:7px"></i></div>
    </div>
    <div class="links"><b>Quick links</b><br>Medical Clinic<br>Pharmacy<br>Home Monitoring<br>Home Healthcare<br>Contact Us<br>Resources<br>Join Our Team</div>
    <div class="loc" style="top:24px"><span><i class="c"></i><b>Medical Clinic</b> - White Rock</span><span>⌄</span></div>
    <div class="loc" style="top:36px"><span><i class="c g"></i><b>Pharmacy</b> - Surrey</span><span>⌃</span></div>
    <div class="abs" style="left:304px;top:50px;font-size:3.6px;line-height:2.3;opacity:.9">+1 (604) 555-0142 &nbsp;&nbsp;&nbsp;&nbsp;&nbsp;&nbsp;&nbsp;&nbsp;&nbsp;&nbsp;+1 (604) 555-0187<br>Medical@HarborlineHealth.ca &nbsp;&nbsp;&nbsp;#109 - 2040 Ferncliff Ave, Surrey BC, V3S 0A1<br>Monday - Friday 11:00AM - 4:30PM</div>
    <div class="loc" style="top:94px"><span><i class="c"></i><b>Medical Clinic</b> - White Rock</span><span>⌄</span></div>
    <div class="loc" style="top:106px"><span><i class="c g"></i><b>Pharmacy</b> - Surrey</span><span>⌄</span></div>
    <div class="legal"><span>© 2025 Harborline Medical. All Rights Reserved</span><span>Privacy Policy &nbsp;|&nbsp; Cookies &nbsp;|&nbsp; Terms And Conditions</span></div>
  </section>
</main>

<!-- ================= MOBILE ================= -->
<main class="mob">
  <section class="m-top">Proudly Canadian and locally owned and operated. Our doctors and nurse practitioners are now accepting new patients.<br><span class="pill">Download Intake Forms</span></section>

  <section class="m-nav">
    <div class="logo-sm"><span class="sq" style="width:10px;height:10px"></span><b style="font-size:10px">Harborline</b><span style="font-size:5px;color:var(--navy);margin-left:3px;line-height:1.2">Medical Clinic<br>Pharmacy</span></div>
    <div class="burger"><i></i><i></i><i></i></div>
  </section>

  <section class="m-hero">
    <div class="w">Welcome to</div>
    <h1>Harborline Medical Clinic</h1>
    <div class="tag">Your Partner In Health</div>
    <p>We are a trusted family doctor in white rock and surrey, committed to offering reliable family doctors in surrey with a focus on providing convenient medical care in surrey.</p>
    <div class="btns"><span class="btn btn-red">Book Appointment</span><span class="btn btn-green">Join Our Team</span></div>
    <div class="photo ph-clinic" role="img" aria-label="Two smiling doctors in white coats in a bright clinic"></div>
    <div class="play" style="left:98px;top:364px"></div>
    <div class="dots" style="left:94px;top:460px"><i class="on"></i><i></i><i></i><i></i></div>
    <div class="abs" style="left:0;right:0;top:604px"></div>
    <div class="abs" style="left:0;right:0;top:478px;font-size:10px;color:var(--navy)">1 / 4</div>
  </section>

  <section class="m-strip">
    <div class="strip-lbl">Member of</div>
    <div class="strip-row"><span class="badge-rect" style="width:76px;height:26px"></span><span class="badge-rect" style="width:80px;height:26px"></span></div>
    <div class="strip-row" style="margin:8px 0 0 60px"><span class="badge" style="width:24px;height:24px"></span></div>
    <div class="strip-lbl" style="margin-top:18px">Licensed by</div>
    <div class="strip-row" style="justify-content:center"><span class="badge-rect" style="width:70px;height:24px"></span><span class="badge" style="width:24px;height:24px"></span></div>
    <div class="strip-row" style="justify-content:center;margin-top:10px"><span class="badge-rect" style="width:70px;height:24px"></span><span class="badge" style="width:24px;height:24px"></span></div>
  </section>

  <section class="m-serv">
    <h2 class="h-title">Our <em>services</em></h2>
    <div class="sub">Convenient, Quality Care in Surrey and White Rock</div>
    <article class="m-card" style="top:69px"><span class="ico"></span><h3>Chronic and<br>complex care</h3><svg class="arrow-ne" style="right:14px;top:16px;width:8px;height:8px" viewBox="0 0 8 8"><path d="M1 7L7 1M3 1h4v4" stroke="#2b2f83" fill="none" stroke-width="1"/></svg><p>Our experienced family doctors in surrey and white rock offer high-quality care for chronic conditions.</p><div class="photo ph-warm" role="img" aria-label="Caregiver assisting an older patient at home"></div></article>
    <article class="m-card" style="top:324px"><span class="ico"></span><h3>Diagnostic<br>investigation</h3><svg class="arrow-ne" style="right:14px;top:16px;width:8px;height:8px" viewBox="0 0 8 8"><path d="M1 7L7 1M3 1h4v4" stroke="#2b2f83" fill="none" stroke-width="1"/></svg><p>Our medical clinic near me provides a wide range of diagnostic tests and procedures to identify potential issues.</p><div class="photo ph-cool" role="img" aria-label="Lab technician working with a microscope"></div></article>
    <article class="m-card" style="top:579px"><span class="ico"></span><h3>Full family care<br>services</h3><svg class="arrow-ne" style="right:14px;top:16px;width:8px;height:8px" viewBox="0 0 8 8"><path d="M1 7L7 1M3 1h4v4" stroke="#2b2f83" fill="none" stroke-width="1"/></svg><p>We offer comprehensive family doctor services for all ages, including adults, prenatal care, youth.</p><div class="photo ph-warm" role="img" aria-label="Family visiting a doctor together"></div></article>
    <span class="btn btn-red center-btn" style="top:834px;font-size:6px;padding:5px 14px">View All Services</span>
  </section>

  <section class="m-mission">
    <h2>Mission <em>statement</em></h2>
    <p>Our mission is to be the best walk-in clinic in Surrey and a top-rated medical clinic in Surrey, leading the way in innovation and patient care. We aim to provide affordable healthcare that is empathetic, efficient, and accessible to all.</p>
  </section>

  <section class="m-about" style="overflow:visible">
    <h2>About <em>us</em></h2>
    <div class="lead">We're an established, forward thinking family practice in white rock/south surrey.</div>
    <div class="strong">We're proud to provide top-notch healthcare services at Harborline in white rock.</div>
    <p>We are a trusted family doctor in White Rock and Surrey, committed to offering reliable family doctors in Surrey with a focus on providing convenient medical care. Our clinic is equipped with the latest technology and staffed by a skilled team dedicated to exceptional care in a safe and supportive environment.</p>
    <span class="btn btn-red" style="font-size:6px;padding:5px 16px;margin-top:14px">Explore More</span>
    <div class="photo ph-team" style="left:10px;top:325px;width:200px;height:250px;z-index:2" role="img" aria-label="Group of doctors and nurses standing together"></div>
    <div class="yrs" style="left:52px;top:314px;padding:4px 10px;font-size:14px">10+<small style="font-size:5.4px;text-align:left">Years of working<br>experience</small></div>
  </section>

  <section class="m-rev">
    <h2 class="h-title">What our <em>client says</em></h2>
    <div class="sub">Harborline Pharmacy &amp; Vaccine Clinic - White Rock/South Surrey</div>
    <div class="score">Excellent <span class="stars">★★★★★</span> 4.9 based on 199 reviews</div>
    <article class="r-card"><span class="g-dot"></span><div class="r-head"><span class="avatar" style="background:var(--green)">M</span><div><b>Mara Ellison</b><small>5 Days Ago</small></div></div><span class="stars">★★★★</span><p>I was able to speak to a doctor, receive a prescription from the doctor through the clinic and pick up my prescription all within one hour! Very pleasant, especially considering the lack of walk-in options nearby.</p></article>
    <span class="circ-arrow" style="left:8px;top:282px;width:14px;height:14px"></span>
    <span class="btn btn-red center-btn" style="top:283px;font-size:6px;padding:4px 14px">View All Review</span>
    <span class="circ-arrow" style="left:198px;top:282px;width:14px;height:14px"></span>
  </section>

  <section class="m-res">
    <h2 class="h-title">Harborline <em>Resources</em></h2>
    <div class="sub">Explore the latest news and resources.</div>
    <article class="b-card" style="top:55px"><div class="photo ph-warm" role="img" aria-label="Toddler sitting at a table with food"></div><div class="dt">Feb 18, 2025</div><h3>Why your toddler won't eat and when to seek care</h3><span class="go"></span></article>
    <article class="b-card" style="top:304px"><div class="photo ph-cool" role="img" aria-label="Doctor talking with a patient"></div><div class="dt">Feb 14, 2025</div><h3>What to do if you don't have a family doctor in white rock, south surrey, and surrey</h3><span class="go"></span></article>
    <article class="b-card" style="top:553px"><div class="photo ph-warm" role="img" aria-label="Nurse checking an older patient at home"></div><div class="dt">Feb 14, 2025</div><h3>Enhancing patient care with Harborline pharmacy's home monitoring program</h3><span class="go"></span></article>
    <span class="btn btn-red center-btn" style="top:812px;font-size:6px;padding:5px 14px">View All Resources</span>
  </section>

  <section class="m-faq">
    <div class="kick">Frequently asked questions</div>
    <h2>Helping you <em>understand</em><br>healthcare</h2>
    <div class="intro">Here to make your experience as seamless as possible: explore answers to common questions about our services, policies, and patient care.</div>
    <div class="faq-list">
      <div class="faq-item"><span>What should I bring to my first appointment?</span><span class="chev">⌃</span></div>
      <div class="faq-ans">For your first visit, please bring a valid ID, your insurance card, any current medications or a list of them, and any relevant medical records.</div>
      <div class="faq-item"><span>How do I schedule an appointment?</span><span class="chev">⌄</span></div>
      <div class="faq-item"><span>What insurance plan do you accept?</span><span class="chev">⌄</span></div>
      <div class="faq-item"><span>Can I get a prescription refill without an appointment?</span><span class="chev">⌄</span></div>
      <div class="faq-item"><span>What should I expect during my first visit?</span><span class="chev">⌄</span></div>
      <div class="faq-item"><span>How are treatment plans customized for individual need?</span><span class="chev">⌄</span></div>
    </div>
    <div class="emerg"><span class="badge"></span><span>We always take care of your smile<br><strong>24/7 Emergency</strong><br>604-555-0199</span></div>
  </section>

  <section class="m-foot">
    <div class="logo">
      <div class="logo-sm" style="gap:6px"><span class="sq" style="width:22px;height:22px"></span><span class="name">Harborline</span></div>
      <div class="tg" style="margin-left:28px">Your Partner in Health</div>
    </div>
    <div class="ql">Quick links</div>
    <div class="cols"><div>Medical Clinic<br>Pharmacy<br>Home Monitoring<br>Home Healthcare</div><div>Contact Us<br>Resources<br>Join Our Team</div></div>
    <div class="loc" style="top:182px"><span><i class="c"></i><b>Medical Clinic</b> - White Rock</span><span>⌄</span></div>
    <div class="loc" style="top:204px"><span><i class="c g"></i><b>Pharmacy</b> - Surrey</span><span>⌃</span></div>
    <div class="det" style="top:224px">+1 (604) 555-0142<br>Medical@HarborlineHealth.ca<br>Monday - Friday 11:00AM - 4:30PM<br>+1 (604) 555-0187<br>#109 - 2040 Ferncliff Ave, Surrey BC, V3S 0A1</div>
    <div class="loc" style="top:340px"><span><i class="c"></i><b>Medical Clinic</b> - White Rock</span><span>⌄</span></div>
    <div class="loc" style="top:362px"><span><i class="c g"></i><b>Pharmacy</b> - Surrey</span><span>⌄</span></div>
    <div class="socials"><i style="width:12px;height:12px"></i><i style="width:12px;height:12px"></i><i style="width:12px;height:12px"></i><i style="width:12px;height:12px"></i></div>
    <div class="legal">Privacy Policy &nbsp;|&nbsp; Cookies &nbsp;|&nbsp; Terms And Conditions<br>© 2025 Harborline Medical. All Rights Reserved</div>
  </section>
</main>

</body>
</html>
```